Wren Motorcar Polishing Flyer Design

Hi, I need a flyer design for the pricing and package display of my business (Wren Motorcar Polishing)

www.kelvora.example/wrenmotorpolish

To keep this short and simple, I will need 2 versions of your finished product, can be similar in design just has to be saying something different.

First flyer will be the general version for all customers.

It will need to include the following!
Format, Placement, Font, Design etc.. is all up to you!

==================================

Package 1 [Cars $49.99][Trucks Vans & SUV's $54.99]: Speed Detail

- Exterior Pressure Clean w/ Spotless water
treatment and Vacuum dried
- Wheel Wells Glossed and Cleaned
- Tires Cleaned and Hand Dried
- Tires Dressed with Gloss Finish
- Exterior and Interior Windows cleaned and Hand Dried
- Interior is Vacuumed and Door jams cleaned to Perfection!

Package 2 [Cars $59.99][Trucks Vans & SUV's $64.99]: Speed Detail & Hand Waxing

- Exterior Pressure Clean w/ Spotless water treatment and Vacuum dried
- Hand Applied Wax Treatment with Delmark's Advanced Spray on wax & Micro Scratch Sealant!

Package 3 [Cars $110.00][Trucks Vans & SUV's $149.99]: Advanced Interior Detail

- Interior & Exterior Windows Cleaned and Hand Dried
- All Vents and Creases cleaned out
- Advanced plastic/vinyl/leather Vellusta Interior Treatment!
- Plastic/Vinyl/Leather Conditioner Vellusta Treatment
- Hand Treated Dust Removal
- Seats/Carpets/Headliner steam cleaned
- Seat Belts/Trunks & Floor Mats Treated and Rejuvenated
- Stain Removal

Package 4 [Cars $110.00][Trucks Vans & SUV's $149.99]: Advanced Exterior Detail

- Exterior Pressure Clean w/ Spotless water treatment and Vacuum dry with additional Hand Drying
- Hand Applied Carnauba Wax & Micro Scratch Sealant Treatment
- Dark Exterior Plastic Restoration Treatment (wherever applicable)

Package 5 [Cars $210][Trucks Vans & SUV's $299.99];The Complete Detail

- Stain Removal

Additional Options (May be applied to existing packages when requested!):

(Clay Bar Treatment): [Cars $69.99][Trucks Vans & SUV's $99.99]

- Removal of all Build-Up on Paint such as Micro debris, stone chips, water spots

(Full Vehicle Polishing): [Cars $75.99][Trucks Vans & SUV's $119.99]

- This process removes marring, swirl marks, scratches, stone chips, water spots and acid etching caused by bird droppings and bug remains.

- Adds a sleek shine when wax is applied after.

(Drop-Q Hand Applied Window Treatment): [Cars $10.00][Trucks Vans & SUV's $15]

- This process repels water, making windshield wipers unneeded during storms and rainy weather.

A percentage of proceeds will be Donated to Help Veterans in need!

Phone #: xxx-xxx-xxxx
Email #: xxxxxxxxxx
Instagram: @
Facebook: kelvora.example/wrenmotorpolish
website: > Coming Soon <

Alright, that will be the first designed flyer.

The next flyer can be single paged or flyer layed out. It is generally aimed towards my first customer Lindqvist Strength and Care. An image of there logo will be provided below along with my logo and current business card so ideas can be drawn beside them.

Wren Motorcar Polishing
The Lindqvist Special (For August)

Package 1 [Cars $24.99][Trucks Vans & SUV's $34.99]: Speed Detail

Package 2 [Cars $39.99][Trucks Vans & SUV's $44.99]: Speed Detail & Hand Waxing

Thanks a TON! If you guy's need anymore information or have any other questions during the design process, please, please; let me know!

Target Market(s)

Automotive Detailing, Mobile Automotive Detailing, Parking Lot Detailing, Business Detailing, etc.

Industry/Entity Type

Automotive

Requirements
Must have
• A Classy Design, I'd like it to match in some form or another the Card pictures I have submitted
Nice to have
• Black and White as primary colors, silver aswell
Should not have
• Not too much Wren orange coloring in the design unless it adds to the overall definition of the finished project. Thanks!

```html
<!DOCTYPE html>
<html lang="en">
<head>
<meta charset="utf-8">
<title>The Lindqvist Special – Wren Motorcar Polishing</title>
<link rel="stylesheet" href="https://fonts.googleapis.com/css2?family=Oswald:wght@500;600&family=Lato:wght@400&display=swap">
<style>
  :root {
    --orange: #f07f22;
    --ink: #141414;
    --panel: #1e1e1e;
    --white: #ffffff;
    --silver-hi: #f2f2f2;
    --silver-mid: #bdbdbd;
    --silver-lo: #7a7a7a;
    --charcoal: #2b2b2b;
    --page: #3a3a3a;
  }
  * { box-sizing: border-box; margin: 0; padding: 0; }
  html, body { width: 1200px; height: 900px; overflow: hidden; }
  body { background: var(--page); position: relative; }

  .flyer {
    position: absolute; left: 283px; top: 20px;
    width: 634px; height: 860px; overflow: hidden;
    background: radial-gradient(ellipse at 50% 40%, var(--panel), var(--ink));
  }
  .flyer__shapes { position: absolute; inset: 0; }

  .month-tag {
    position: absolute; left: 84px; top: 68px;
    transform: translate(-50%, -50%) rotate(-40deg);
    font: 500 30px/1 "Oswald", sans-serif; color: var(--white);
    text-transform: uppercase; white-space: nowrap;
  }
  .special-title {
    position: absolute; left: 120px; top: 58px; width: 300px;
    text-align: center; color: var(--orange); white-space: nowrap;
    font: 600 44px/62px "Oswald", sans-serif; text-transform: uppercase;
  }
  .brand-name {
    position: absolute; left: 430px; top: 62px; width: 200px;
    text-align: center; color: var(--charcoal);
    font: 600 26px/30px "Oswald", sans-serif; text-transform: uppercase;
  }

  .package {
    position: absolute; left: 24px; width: 592px;
    border: 3px solid var(--orange); border-radius: 9px;
    padding: 4px 14px 0 14px;
  }
  .package--one { top: 242px; height: 248px; }
  .package--two { top: 503px; height: 292px; }
  .package__label, .package__name {
    color: var(--orange); font: 500 25px/30px "Oswald", sans-serif;
    text-transform: uppercase;
  }
  .price-bar {
    height: 38px; margin: 2px 0 4px -4px; border-radius: 6px;
    background: linear-gradient(var(--silver-hi), var(--silver-mid) 55%, var(--silver-lo));
    box-shadow: 0 3px 6px rgba(0,0,0,.6);
    display: flex; align-items: center; justify-content: space-between;
    padding: 0 12px 0 8px;
    font: 600 25px/1 "Oswald", sans-serif; color: var(--ink);
    letter-spacing: -0.3px;
    text-transform: uppercase; white-space: nowrap; overflow: hidden;
  }
  .features { list-style: none; margin-top: 2px; }
  .features li {
    position: relative; padding-left: 28px;
    font: 400 14.5px/22.6px "Lato", sans-serif; color: var(--white);
  }
  .features li::before {
    content: "✹"; position: absolute; left: 9px; top: 0;
    color: var(--orange); font-size: 13px;
  }

  .donation {
    position: absolute; left: 0; top: 808px; width: 634px; height: 52px;
    background: var(--orange); border-top: 3px solid var(--white);
  }
  .donation__text {
    position: absolute; left: 20px; top: 4px; width: 496px;
    text-align: center; color: var(--white);
    font: 500 20px/20px "Oswald", sans-serif; text-transform: uppercase;
  }
  .partner-name {
    position: absolute; left: 520px; top: 0; width: 91px; height: 49px;
    background: var(--white); display: flex; align-items: center;
    justify-content: center; text-align: center;
    color: var(--charcoal); font: 600 12px/13px "Oswald", sans-serif;
    text-transform: uppercase;
  }
</style>
</head>
<body>
  <main class="flyer">
    <svg class="flyer__shapes" width="634" height="860" viewBox="0 0 634 860" aria-hidden="true">
      <polygon points="196,0 235,0 0,166 0,139" fill="var(--orange)"/>
      <polygon points="238,0 244,0 0,172 0,168" fill="var(--white)"/>
      <polygon points="420,0 634,0 634,170 398,197" fill="var(--white)"/>
      <polygon points="0,214 634,168 634,200 0,226" fill="var(--orange)"/>
      <polygon points="0,229 634,203 634,207 0,233" fill="var(--white)"/>
    </svg>

    <div class="month-tag">For August</div>
    <h1 class="special-title">The Lindqvist<br>Special</h1>
    <div class="brand-name">Wren Motorcar Polishing</div>

    <section class="package package--one">
      <h2 class="package__label">Package 1</h2>
      <div class="price-bar"><span>[Cars $24.99]</span><span>[Trucks Vans &amp; SUV's $34.99]</span></div>
      <h3 class="package__name">Speed Detail:</h3>
      <ul class="features">
        <li>Exterior Pressure Clean w/ Spotless water treatment and Vacuum dried</li>
        <li>Wheel Wells Glossed and Cleaned</li>
        <li>Tires Cleaned and Hand Dried</li>
        <li>Tires Dressed with Gloss Finish</li>
        <li>Exterior and Interior Windows cleaned and Hand Dried</li>
        <li>Interior is Vacuumed and Door jams cleaned to Perfection!</li>
      </ul>
    </section>

    <section class="package package--two">
      <h2 class="package__label">Package 2</h2>
      <div class="price-bar"><span>[Cars $39.99]</span><span>[Trucks Vans &amp; SUV's $44.99]</span></div>
      <h3 class="package__name">Speed Detail &amp; Hand Waxing</h3>
      <ul class="features">
        <li>Exterior Pressure Clean w/ Spotless water treatment and Vacuum dried</li>
        <li>Wheel Wells Glossed and Cleaned</li>
        <li>Tires Cleaned and Hand Dried</li>
        <li>Tires Dressed with Gloss Finish</li>
        <li>Exterior and Interior Windows cleaned and Hand Dried</li>
        <li>Interior is Vacuumed and Door jams cleaned to Perfection!</li>
        <li>Hand Applied Wax Treatment with Delmark's Advanced Spray on wax &amp;<br>Micro Scratch Sealant!</li>
      </ul>
    </section>

    <footer class="donation">
      <p class="donation__text">A percentage of proceeds will be donated to help<br>veterans in need!</p>
      <div class="partner-name">Lindqvist Strength and Care</div>
    </footer>
  </main>
</body>
</html>
```